Business card design for Bront Engineering Qavo

We need a new business card design along with all the necessary to place an order. The company is Bront Engineering Qavo and we recently updated our logo.

```html
<!DOCTYPE html>
<html lang="en">
<head>
<meta charset="UTF-8">
<title>Bront Engineering Qavo – Business Card</title>
<link rel="stylesheet" href="https://fonts.googleapis.com/css2?family=Arimo:wght@400;700&family=Montserrat:wght@500;600&display=swap">
<style>
  :root {
    --backdrop: #2d2d2d;
    --card: #000000;
    --accent: #e3bd24;
    --steel: #8f8f8f;
    --ink: #ffffff;
  }
  * { margin: 0; padding: 0; box-sizing: border-box; }
  html, body {
    width: 1200px; height: 1015px; overflow: hidden;
    background: var(--backdrop);
  }
  .canvas { position: relative; width: 1200px; height: 1015px; }
  .card {
    position: absolute; width: 540px; height: 308px;
    background: var(--card); overflow: hidden;
    box-shadow: 0 12px 30px rgba(0,0,0,.45);
  }
  .card-front { left: 330px; top: 150px; }
  .card-back { left: 330px; top: 545px; }
  .edge-band {
    position: absolute; left: 0; right: 0; bottom: 0; height: 9px;
    background: var(--accent);
  }
  .brand {
    position: absolute; left: 0; right: 0; top: 128px;
    display: flex; align-items: center; justify-content: center; gap: 12px;
  }
  .brand-mark { width: 14px; height: 14px; background: var(--accent); }
  .brand-name {
    font-family: "Montserrat", sans-serif; font-weight: 600;
    font-size: 26px; letter-spacing: 2px; color: var(--steel);
    text-transform: uppercase;
  }
  .contact {
    position: absolute; left: 40px; top: 44px;
    font-family: "Arimo", sans-serif; color: var(--ink);
  }
  .person-name {
    font-weight: 700; font-size: 21px; color: var(--accent);
    text-transform: uppercase; letter-spacing: .3px;
  }
  .person-role { font-size: 13px; text-transform: uppercase; margin-top: 3px; letter-spacing: .4px; }
  .divider { width: 90px; height: 1px; background: var(--accent); margin: 14px 0; }
  .detail-list { list-style: none; }
  .detail-list li {
    display: flex; align-items: center; gap: 10px;
    font-size: 14px; line-height: 22px;
  }
  .detail-list svg { width: 14px; height: 14px; flex: none; }
  .address { font-size: 14px; line-height: 20px; }
</style>
</head>
<body>
<main class="canvas">
  <section class="card card-front">
    <div class="brand">
      <span class="brand-mark"></span>
      <span class="brand-name">Bront Engineering Qavo</span>
    </div>
    <div class="edge-band"></div>
  </section>

  <section class="card card-back">
    <div class="contact">
      <p class="person-name">Marcus Hale</p>
      <p class="person-role">Managing Director</p>
      <div class="divider"></div>
      <ul class="detail-list">
        <li>
          <svg viewBox="0 0 24 24" aria-hidden="true"><path fill="var(--accent)" d="M6.6 10.8a15 15 0 0 0 6.6 6.6l2.2-2.2a1 1 0 0 1 1-.25 11.4 11.4 0 0 0 3.6.57 1 1 0 0 1 1 1V20a1 1 0 0 1-1 1A17 17 0 0 1 3 4a1 1 0 0 1 1-1h3.5a1 1 0 0 1 1 1c0 1.25.2 2.45.57 3.6a1 1 0 0 1-.25 1z"/></svg>
          044-987 654 321
        </li>
        <li>
          <svg viewBox="0 0 24 24" aria-hidden="true"><path fill="var(--accent)" d="M2 5h20v14H2z"/><path fill="none" stroke="#000" stroke-width="1.8" d="M2 5l10 8 10-8"/></svg>
          info@brontqavo.com
        </li>
        <li>
          <svg viewBox="0 0 24 24" aria-hidden="true"><g fill="none" stroke="var(--accent)" stroke-width="2"><circle cx="12" cy="12" r="10"/><ellipse cx="12" cy="12" rx="4.5" ry="10"/><path d="M2 12h20M4 7h16M4 17h16"/></g></svg>
          www.brontqavo.com
        </li>
      </ul>
      <div class="divider"></div>
      <p class="address">17, Harrow Field Road<br>30718, Eastvale</p>
    </div>
    <div class="edge-band"></div>
  </section>
</main>
</body>
</html>
```